Business Card Design

Copperfield Lantern & Spark, Inc. (CLS), located in Memphis, TN began operating on 2003. We are a certified
minority woman-owned business that genuinely takes a vested interest in our customers. We serve utilities,
government, contractors and end user markets in electrical, water, gas and industrial supplies. Our core
competency as a distributor of electrical materials has positioned us to serve business of all size. As your supply
chain partner, we arm you with the resources you need to make your supply chain more efficient. Our team
works with your team on a daily basis to help you solve problems and achieve goals. This team approach has
helped CLS customers to succeed and we can do the same for you.

NAICS Codes:
423610 Electrical Apparatus and Equipment, Wiring Supplies, and Related Equipment Merchant
Wholesalers
423510 Metal Service Centers and Other Metal Merchant Wholesalers
423720 Plumbing and Heating Equipment and Supplies (Hydronics) Merchant Wholesalers

Certifications
MBE (KRVPQAL, State of Tennessee Up-MRX and FJW), WBE (HQOLT),
WOSB, DOT (TDOT, MDOT, ALDOT, SCDOT, NCDOT, and VDOT), LOSB,
SBE, and LSB Certified
Some of Our Products Include:
. Boxes & Covers
. Conduit & Raceway
. Fittings
. Fuses
. Lamp & Ballasts
. Lighting Controls & Timers
. Lighting Fixtures
. Personal Safety
. Pipes
. Power Distribution
. Terminations Ground & Splices
. Tools & Testers
. Wire, Cords & Cable
. Wiring Devices
. Valves

Industry/Entity Type

Business

Contact Information for Business Card

Marianne T. Holloway - President/CEO
4728 Quillon Ave., Memphis, TN 38127
901-555-0147 office, 901-555-0182 fax, 901-555-0163 cell
mtholloway@clsllc-example.com - www.clsincorp-example.com

```html
<!DOCTYPE html>
<html lang="en">
<head>
<meta charset="utf-8">
<title>Copperfield Lantern &amp; Spark — Business Card</title>
<link rel="stylesheet" href="https://fonts.googleapis.com/css2?family=Open+Sans:wght@400;600&display=swap">
<style>
  :root {
    --stage: #d9d6d2;
    --card: #0d0d0d;
    --ink: #f2f2f2;
    --ink-soft: #d6d6d6;
    --accent: #e6e01e;
  }
  * { box-sizing: border-box; margin: 0; padding: 0; }
  html, body { width: 1200px; height: 900px; overflow: hidden; }
  body {
    background: var(--stage);
    font-family: "Open Sans", Arial, sans-serif;
    display: flex;
    align-items: center;
    justify-content: center;
    gap: 50px;
  }
  .card {
    width: 525px;
    height: 300px;
    background: var(--card);
    color: var(--ink);
    position: relative;
    box-shadow: 0 6px 18px rgba(0,0,0,.25);
  }
  .wordmark {
    display: flex;
    align-items: center;
    gap: 8px;
    color: var(--ink);
    font-weight: 400;
    font-size: 17px;
    letter-spacing: .5px;
    line-height: 1.15;
  }
  .wordmark-square {
    width: 14px; height: 14px;
    background: var(--ink);
    flex: none;
  }

  /* Front */
  .card-front .wordmark {
    position: absolute;
    left: 40px; top: 178px;
    width: 210px;
  }
  .card-front .divider {
    position: absolute;
    left: 268px; top: 62px;
    width: 1px; height: 190px;
    background: var(--accent);
  }
  .contact {
    position: absolute;
    left: 284px; top: 60px;
    font-size: 12.5px;
    line-height: 1.35;
    color: var(--ink-soft);
  }
  .contact-name { color: var(--accent); font-weight: 600; font-size: 15px; }
  .contact-title { margin-bottom: 12px; }
  .contact-address { margin-bottom: 12px; }
  .contact-list { list-style: none; }
  .contact-list li { display: flex; align-items: center; gap: 8px; }
  .contact-list svg { width: 11px; height: 11px; fill: var(--accent); flex: none; }

  /* Back */
  .card-back .wordmark {
    position: absolute;
    left: 0; right: 0; top: 44px;
    justify-content: center;
    font-size: 19px;
  }
  .products {
    position: absolute;
    left: 50px; right: 30px; top: 110px;
    display: grid;
    grid-template-columns: 1fr 1fr;
    column-gap: 14px;
    font-size: 12.5px;
    line-height: 1.4;
    color: var(--ink-soft);
    list-style: none;
  }
  .products-left { text-align: right; list-style: none; }
  .products-right { list-style: none; }
  .products-left .gap { margin-top: 18px; }
</style>
</head>
<body>

  <section class="card card-front" aria-label="Business card front">
    <div class="wordmark"><span class="wordmark-square"></span><span>Copperfield Lantern &amp; Spark</span></div>
    <div class="divider"></div>
    <div class="contact">
      <p class="contact-name">Marianne T. Holloway</p>
      <p class="contact-title">President/CEO</p>
      <p class="contact-address">4728 Quillon Ave., Memphis<br>TN 38127</p>
      <ul class="contact-list">
        <li><svg viewBox="0 0 24 24" aria-hidden="true"><path d="M6.6 10.8a15 15 0 0 0 6.6 6.6l2.2-2.2a1 1 0 0 1 1-.25 11.4 11.4 0 0 0 3.6.6 1 1 0 0 1 1 1V20a1 1 0 0 1-1 1A17 17 0 0 1 3 4a1 1 0 0 1 1-1h3.5a1 1 0 0 1 1 1c0 1.25.2 2.45.6 3.6a1 1 0 0 1-.25 1z"/></svg>901-555-0147</li>
        <li><svg viewBox="0 0 24 24" aria-hidden="true"><path d="M6 2h10v5H6zM4 8h16a2 2 0 0 1 2 2v10H2V10a2 2 0 0 1 2-2zm3 4v2h4v-2zm0 4v2h10v-2z"/></svg>901-555-0182</li>
        <li><svg viewBox="0 0 24 24" aria-hidden="true"><path d="M7 1h10a2 2 0 0 1 2 2v18a2 2 0 0 1-2 2H7a2 2 0 0 1-2-2V3a2 2 0 0 1 2-2zm0 3v14h10V4zm5 15.5a1 1 0 1 0 0 2 1 1 0 0 0 0-2z"/></svg>901-555-0163</li>
        <li><svg viewBox="0 0 24 24" aria-hidden="true"><path d="M2 5h20v14H2zm2 2v.5l8 5 8-5V7z"/></svg>mtholloway@clsllc-example.com</li>
        <li><svg viewBox="0 0 24 24" aria-hidden="true"><path d="M12 2a10 10 0 1 0 0 20 10 10 0 0 0 0-20zm0 2c1 0 2.3 2 2.8 5H9.2C9.7 6 11 4 12 4zM4.3 11h3.8a18 18 0 0 0 0 2H4.3a8 8 0 0 1 0-2zm11.6 0h3.8a8 8 0 0 1 0 2h-3.8a18 18 0 0 0 0-2zM9.2 15h5.6c-.5 3-1.8 5-2.8 5s-2.3-2-2.8-5z"/></svg>www.clsincorp-example.com</li>
      </ul>
    </div>
  </section>

  <section class="card card-back" aria-label="Business card back">
    <div class="wordmark"><span class="wordmark-square"></span><span>Copperfield Lantern &amp; Spark</span></div>
    <div class="products">
      <ul class="products-left">
        <li>Boxes &amp; Covers</li>
        <li>Conduit &amp; Raceway</li>
        <li>Fittings</li>
        <li>Fuses</li>
        <li class="gap">Lamp &amp; Ballasts</li>
        <li>Lighting Controls &amp; Timers</li>
        <li>Lighting Fixtures</li>
      </ul>
      <ul class="products-right">
        <li>Personal Safety</li>
        <li>Pipes</li>
        <li>Power Distribution</li>
        <li>Terminations Ground &amp; Splices</li>
        <li>Tools &amp; Testers</li>
        <li>Wire, Cords &amp; Cable</li>
        <li>Wiring Devices</li>
        <li>Valves</li>
      </ul>
    </div>
  </section>

</body>
</html>
```